Business Card design for new private practice opening

I need a business card design for my new private practice with my new logo uploaded as a file
On the front the logo
On the back: maybe a small logo somewhere?
Priv. Doz. DDr. Corinna Vestaluk
Fachärztin für Allgemein- & Viszeralchirurgie
Address: xxx
Tel: xxx
Mobil:xxx
Webseite:xxx
Email:xxx

Contact Information for Business Card

See project description above for details

Requirements
Nice to have
• I would like the colors of the logo incorporated into the business card

```html
<!DOCTYPE html>
<html lang="de">
<head>
<meta charset="utf-8">
<title>Vestaluk Chirurgie – Visitenkarte</title>
<link rel="stylesheet" href="https://fonts.googleapis.com/css2?family=Montserrat:wght@500;600&family=Arimo:wght@400&display=swap">
<style>
  :root {
    --backdrop: #5a5a5a;
    --card-white: #ffffff;
    --teal: #47bab7;
    --teal-deep: #3aa9a6;
    --teal-light: #6fcfcb;
    --ink-grey: #808080;
    --text-grey: #4a4a4a;
    --white: #ffffff;
  }
  * { margin: 0; padding: 0; box-sizing: border-box; }
  html, body {
    width: 1200px; height: 1200px; overflow: hidden;
    background: var(--backdrop);
  }
  .canvas { position: relative; width: 1200px; height: 1200px; }

  .card { position: absolute; left: 258px; width: 690px; height: 394px; }
  .card-front { top: 158px; background: var(--card-white); }
  .card-back  { top: 651px; background: var(--teal); }

  .name-line {
    position: absolute; left: 50px; top: 64px;
    font-family: "Montserrat", sans-serif; font-weight: 600;
    color: var(--ink-grey); white-space: nowrap;
  }
  .name-line .title { font-size: 16px; }
  .name-line .name { font-size: 25px; text-transform: uppercase; letter-spacing: 0.2px; }
  .specialty {
    position: absolute; left: 50px; top: 95px;
    font-family: "Arimo", sans-serif; font-size: 15px; color: var(--teal);
  }

  .address {
    position: absolute; left: 50px; top: 180px;
    font-family: "Arimo", sans-serif; font-size: 16px; line-height: 21px;
    color: var(--text-grey); font-style: normal;
  }
  .contact-list {
    position: absolute; left: 50px; top: 237px; list-style: none;
    font-family: "Arimo", sans-serif; font-size: 16px; color: var(--text-grey);
  }
  .contact-list li { display: flex; align-items: center; height: 20.5px; }
  .contact-list svg { width: 14px; height: 14px; margin-right: 11px; fill: var(--teal); }

  .brand {
    position: absolute; left: 380px; top: 243px;
    display: flex; align-items: center;
  }
  .brand-dot {
    width: 74px; height: 74px; border-radius: 50%;
    border: 2px solid var(--ink-grey); margin-right: 14px;
  }
  .brand-name {
    font-family: "Montserrat", sans-serif; font-weight: 600;
    font-size: 27px; line-height: 31px; color: var(--ink-grey);
    text-transform: uppercase; letter-spacing: 0.5px;
  }

  .back-mark {
    position: absolute; left: 232px; top: 81px;
    width: 230px; height: 230px; border-radius: 50%;
    background: var(--teal-deep);
    display: flex; align-items: center; justify-content: center; text-align: center;
    font-family: "Montserrat", sans-serif; font-weight: 600;
    font-size: 22px; line-height: 27px; color: var(--teal-light);
    text-transform: uppercase; letter-spacing: 0.5px;
  }
  .back-web {
    position: absolute; left: 0; right: 0; top: 334px; text-align: center;
    font-family: "Arimo", sans-serif; font-size: 16px; color: var(--white);
  }
</style>
</head>
<body>
<main class="canvas">
  <section class="card card-front">
    <h1 class="name-line"><span class="title">Priv. Doz. DDr.</span> <span class="name">Corinna Vestaluk</span></h1>
    <p class="specialty">Fachärztin für Allgemein- &amp; Viszeralchirurgie</p>

    <address class="address">4210 Lindenweg Lane<br>Greenfield, Canada 52819</address>

    <ul class="contact-list">
      <li><svg viewBox="0 0 16 16" aria-hidden="true"><path d="M3.5 1.2l2.3-.5 1.4 3.3-1.6 1.2c.8 1.8 2.2 3.2 4 4l1.2-1.6 3.3 1.4-.5 2.3c-.2.8-.9 1.3-1.7 1.2C6.5 12 4 9.5 2.3 2.9c-.1-.8.4-1.5 1.2-1.7z"/></svg>555-210-4837</li>
      <li><svg viewBox="0 0 16 16" aria-hidden="true"><path d="M4.5 0h7A1.5 1.5 0 0 1 13 1.5v13a1.5 1.5 0 0 1-1.5 1.5h-7A1.5 1.5 0 0 1 3 14.5v-13A1.5 1.5 0 0 1 4.5 0zm.3 2v10.5h6.4V2zM8 13.3a.9.9 0 1 0 0 1.8.9.9 0 0 0 0-1.8z"/></svg>555-382-9165</li>
      <li><svg viewBox="0 0 16 16" aria-hidden="true"><path d="M1 3.5h14v9H1zm1.4 1.2L8 9l5.6-4.3zM2.2 11.3h11.6L10 7.8 8 9.4 6 7.8z"/></svg>info@Vestalukchirurgie.com</li>
      <li><svg viewBox="0 0 16 16" aria-hidden="true"><path d="M8 1a7 7 0 1 0 0 14A7 7 0 0 0 8 1zm-1 2.2c.6.8.2 1.6-.6 2-.9.4-1.2 1.3-.6 2 .7.8 1.9.5 2.3 1.5.3.8-.3 1.7-.1 2.6.2.8-.3 1.4-1 1.5A5.6 5.6 0 0 1 7 3.2zm4.2 1.4a5.5 5.5 0 0 1 2.1 4.8c-.9-.2-1.5-1-1.6-2-.2-1.2-1.3-1.5-.5-2.8z"/></svg>www.Vestalukchirurgie.com</li>
    </ul>

    <div class="brand">
      <div class="brand-dot" aria-hidden="true"></div>
      <p class="brand-name">Vestaluk<br>Chirurgie</p>
    </div>
  </section>

  <section class="card card-back">
    <p class="back-mark">Vestaluk<br>Chirurgie</p>
    <p class="back-web">www.Vestalukchirurgie.com</p>
  </section>
</main>
</body>
</html>
```